Veterinary Business cards

Redesign Business Card

Information needed on Card:
Hours: Mon-Fri: 4pm -10PM; Sat- Sun- 10 AM- 5PM
Help@bayfernvet.com
www.bayfernvet.com
555-718-2946
4173 SE 19th Ave. okc, ok 73958
*No appointment necessary*

Optional:
Our tag line is "We're here when you need us" - If it fits on the cards.

```html
<!DOCTYPE html>
<html lang="en">
<head>
<meta charset="utf-8">
<title>Bayfern Vet Urgent Care – Business Card Draft</title>
<link href="https://fonts.googleapis.com/css2?family=Arimo:wght@400;700&display=swap" rel="stylesheet">
<style>
  :root {
    --page: #eceded;
    --navy: #062a80;
    --orange: #dc6500;
    --white: #ffffff;
    --ink: #0b0b0b;
    --glow: rgba(40, 90, 220, 0.75);
    --warm-shadow: rgba(90, 35, 0, 0.55);
  }
  * { box-sizing: border-box; margin: 0; padding: 0; }
  html, body {
    width: 893px;
    height: 1200px;
    overflow: hidden;
    background: var(--page);
    font-family: "Arimo", Arial, sans-serif;
    color: var(--white);
  }
  .sheet { position: relative; width: 893px; height: 1200px; }

  .card {
    position: absolute;
    left: 44px;
    width: 782px;
    height: 452px;
  }
  .card--front { top: 41px; background: var(--navy); }
  .card--back { top: 539px; background: var(--orange); }

  .card--front .line { text-shadow: 0 0 4px var(--glow), 1px 1px 2px rgba(0,0,0,0.35); }

  .brand {
    position: absolute;
    left: 20px;
    top: 30px;
    width: 200px;
    text-align: center;
  }
  .brand__name {
    font-size: 24px;
    font-weight: 400;
    letter-spacing: 1px;
    line-height: 1.05;
    color: var(--white);
  }
  .brand__tagline {
    position: absolute;
    left: 158px;
    top: 81px;
    transform: translateX(-50%);
    white-space: nowrap;
    font-size: 15px;
  }

  .hours {
    position: absolute;
    left: 638px;
    top: 31px;
    transform: translateX(-50%);
    text-align: center;
    font-size: 20px;
    line-height: 21px;
    white-space: nowrap;
  }

  .contact {
    position: absolute;
    left: 391px;
    transform: translateX(-50%);
    white-space: nowrap;
    text-align: center;
  }
  .contact--phone { top: 197px; font-size: 68px; line-height: 76px; }
  .contact--email { top: 273px; font-size: 32px; line-height: 38px; }
  .contact--note { top: 325px; font-size: 16px; line-height: 18px; }

  .address {
    position: absolute;
    left: 15px;
    top: 418px;
    font-size: 17px;
    white-space: nowrap;
  }
  .website {
    position: absolute;
    right: 26px;
    top: 406px;
    font-size: 22px;
    white-space: nowrap;
  }

  .skyline {
    position: absolute;
    left: 143px;
    top: 42px;
    width: 496px;
    height: 146px;
    background: linear-gradient(to bottom, rgba(255,255,255,0.18), rgba(255,255,255,0.06));
  }

  .back-brand {
    position: absolute;
    left: 143px;
    top: 196px;
    width: 496px;
    text-align: center;
    color: var(--navy);
    font-weight: 700;
  }
  .back-brand__name { font-size: 58px; line-height: 62px; }
  .back-brand__sub { font-size: 30px; line-height: 34px; letter-spacing: 3px; }

  .back-tagline {
    position: absolute;
    left: 391px;
    top: 308px;
    transform: translateX(-50%);
    white-space: nowrap;
    font-size: 32px;
    line-height: 38px;
    text-shadow: 1px 1px 2px var(--warm-shadow);
  }
  .back-note {
    position: absolute;
    left: 391px;
    top: 382px;
    transform: translateX(-50%);
    white-space: nowrap;
    font-size: 23px;
    line-height: 28px;
    text-shadow: 1px 1px 2px var(--warm-shadow);
  }

  .draft-label {
    position: absolute;
    left: 514px;
    top: 1056px;
    width: 379px;
    height: 85px;
    background: var(--ink);
    padding: 9px 11px;
    font-size: 19px;
    line-height: 22px;
  }
</style>
</head>
<body>
<main class="sheet">

  <section class="card card--front" aria-label="Card front">
    <div class="brand">
      <p class="brand__name">Bayfern Vet Urgent Care</p>
    </div>
    <p class="brand__tagline line">WE'RE HERE WHEN YOU NEED US</p>

    <div class="hours line">
      <p>Hours</p>
      <p>Mon-Fri: 4pm - 10pm</p>
      <p>Sat - Sun: 10am - 5pm</p>
    </div>

    <p class="contact contact--phone line">555-718-2946</p>
    <p class="contact contact--email line">help@bayfernvet.com</p>
    <p class="contact contact--note line">*No Appointment Necessary*</p>

    <p class="address line">4173 SE 19th Ave. okc, oc 73958</p>
    <p class="website line">www.bayfernvet.com</p>
  </section>

  <section class="card card--back" aria-label="Card back">
    <div class="skyline" role="img" aria-label="White outline illustration of a city skyline"></div>
    <div class="back-brand">
      <p class="back-brand__name">Bayfern Vet</p>
      <p class="back-brand__sub">URGENT CARE</p>
    </div>
    <p class="back-tagline">WE'RE HERE WHEN YOU NEED US</p>
    <p class="back-note">*No Appointment Necessary*</p>
  </section>

  <aside class="draft-label">
    <p>DRAFT 1:</p>
    <p>First version for proof of concept</p>
    <p>for the 1st round of feedback</p>
  </aside>

</main>
</body>
</html>
```